New, clean letterhead for law firm in Colorado using recently designed logo.

Professional letterhead for established law firm rebranding. We service high end clientele with mostly family law and personal injury cases. Need source files for future changes. Prefer logo at top, names of members and staff in left margin, contact info in footer.

Target Market(s)

High wealth individuals

Contact Information for Business Card

Need options for traditional and square two sided business cards

Font styles to use
Serif

Colors
0555a3

Requirements
Must have
• Our logo; blue, gray, and white; modern feel.
Should not have
• Images of people

```html
<!DOCTYPE html>
<html lang="en">
<head>
<meta charset="utf-8">
<title>Alderwood Crane Law — Business Card</title>
<link href="https://fonts.googleapis.com/css2?family=Cinzel:wght@500&family=Roboto:wght@400;700&display=swap" rel="stylesheet">
<style>
  :root {
    --brand-blue: #2f6ca6;
    --brand-gray: #9a9a9a;
    --text-gray: #5a5a5a;
    --card-white: #f7f7f7;
    --page-bg: #e9eaec;
  }
  * { box-sizing: border-box; margin: 0; padding: 0; }
  html, body {
    width: 1200px; height: 994px; overflow: hidden;
    background: var(--page-bg);
  }
  .sheet {
    width: 1200px; height: 994px;
    display: flex; align-items: center; justify-content: center; gap: 40px;
  }
  .card {
    position: relative;
    width: 520px; height: 297px;
    overflow: hidden;
    box-shadow: 0 2px 6px rgba(0,0,0,0.12);
  }
  .card-front { background: var(--card-white); }
  .card-back {
    background: var(--brand-blue);
    display: flex; align-items: center; justify-content: center;
  }

  .firm-name {
    font-family: "Cinzel", serif;
    font-weight: 500;
    text-align: center;
    line-height: 1.25;
    letter-spacing: 0.06em;
  }
  .card-front .firm-name {
    position: absolute; left: 24px; top: 98px; width: 240px;
    color: var(--brand-blue); font-size: 19px;
  }
  .card-back .firm-name {
    color: #ffffff; font-size: 30px;
  }
  .firm-name .firm-suffix { display: block; font-size: 0.62em; letter-spacing: 0.2em; }

  .divider {
    position: absolute; left: 282px; top: 62px;
    width: 1.5px; height: 150px; background: var(--brand-blue);
  }

  .contact {
    position: absolute; left: 300px; top: 62px;
    font-family: "Roboto", sans-serif; color: var(--text-gray);
    font-size: 12.5px; line-height: 1.45;
  }
  .contact .person-name {
    color: var(--brand-blue); font-weight: 700; font-size: 15px;
    letter-spacing: 0.03em; text-transform: uppercase;
  }
  .contact .person-title { font-weight: 700; font-size: 13.5px; margin-bottom: 4px; }
  .contact .contact-line { display: flex; align-items: center; gap: 6px; }
  .contact .contact-line svg { width: 12px; height: 12px; fill: var(--brand-blue); flex: none; }

  .footer-band { position: absolute; left: 0; bottom: 0; width: 520px; height: 34px; }
  .website {
    position: absolute; right: 34px; bottom: 9px;
    font-family: "Roboto", sans-serif; font-size: 14px; color: #ffffff;
    letter-spacing: 0.03em;
  }
</style>
</head>
<body>
<main class="sheet">
  <section class="card card-front" aria-label="Business card front">
    <h1 class="firm-name">Alderwood Crane<span class="firm-suffix">Law, LLC</span></h1>
    <div class="divider"></div>
    <div class="contact">
      <p class="person-name">Marcus Ellery</p>
      <p class="person-title">Managing Director</p>
      <p>42 Juniper Ridge Rd, Evergreen</p>
      <p>CO USA 80439</p>
      <p class="contact-line">
        <svg viewBox="0 0 24 24" aria-hidden="true"><path d="M6.6 10.8a15 15 0 0 0 6.6 6.6l2.2-2.2c.3-.3.7-.4 1-.2 1.1.4 2.3.6 3.6.6.6 0 1 .4 1 1V20c0 .6-.4 1-1 1A17 17 0 0 1 3 4c0-.6.4-1 1-1h3.5c.6 0 1 .4 1 1 0 1.3.2 2.5.6 3.6.1.3 0 .7-.2 1z"/></svg>
        3035550172
      </p>
      <p class="contact-line">
        <svg viewBox="0 0 24 24" aria-hidden="true"><path d="M2 5h20v14H2zM3.5 6.5 12 13l8.5-6.5z"/></svg>
        hello@alderwoodcrane.com
      </p>
    </div>
    <svg class="footer-band" viewBox="0 0 520 34" aria-hidden="true">
      <rect x="0" y="24" width="250" height="10" fill="var(--brand-gray)"/>
      <polygon points="232,34 262,0 520,0 520,34" fill="var(--brand-blue)"/>
    </svg>
    <p class="website">www.alderwoodcrane.com</p>
  </section>

  <section class="card card-back" aria-label="Business card back">
    <h2 class="firm-name">Alderwood Crane<span class="firm-suffix">Law, LLC</span></h2>
  </section>
</main>
</body>
</html>
```